Website Refresh

Current Website is CourtFray.net - would like to refresh it up along with adding a few features to it. We have promotional videos that are currently on our Facebook page that we would like to have on our website . We also need a page of information that the users can interactive with in making choices for themselves. For instance finding their name on the list and picking one of three options for a time.

Target Market(s)

Tennis Players - Male and Female Ages 30-80

Coding

Coded - Design and coding required

Number of Pages Required

5+ page

Requirements
Must have
• Same content, with new functionality for users to make choices. Most match logo and icon

```html
<!DOCTYPE html>
<html lang="en">
<head>
<meta charset="utf-8">
<title>Court Fray – Competitive Tennis Tournaments For Adults</title>
<link href="https://fonts.googleapis.com/css2?family=Poppins:wght@300;400;500;600;700;800&display=swap" rel="stylesheet">
<style>
  :root {
    --lime: #b3c52f;
    --lime-dark: #a4b627;
    --ink: #1f1f1f;
    --text: #3a3a3a;
    --white: #ffffff;
    --hero-a: #3b3d38;
    --hero-b: #2b2d2a;
    --card-a: #f3f3f3;
    --card-b: #ececec;
    --line: #cfcfcf;
  }
  * { box-sizing: border-box; margin: 0; padding: 0; }
  html, body { width: 938px; height: 1200px; overflow: hidden; background: var(--white); }
  body { position: relative; font-family: "Poppins", sans-serif; color: var(--text); }

  .hero {
    position: absolute; left: 0; top: 0; width: 938px; height: 516px;
    background: linear-gradient(180deg, #404a3c 0%, var(--hero-a) 30%, #4a4743 55%, var(--hero-b) 100%);
  }
  .hero-photo {
    position: absolute; inset: 0;
    background:
      radial-gradient(ellipse 120px 200px at 700px 200px, rgba(200,190,180,.22), transparent 70%),
      linear-gradient(180deg, rgba(90,100,120,.35) 0%, rgba(60,60,60,0) 35%, rgba(80,70,60,.25) 50%, rgba(0,0,0,0) 70%);
  }

  .brand {
    position: absolute; left: 20px; top: 24px; display: flex; align-items: center; gap: 6px;
    font-weight: 700; font-size: 17px; color: var(--white);
  }
  .brand-dot { width: 10px; height: 10px; border-radius: 50%; background: var(--lime); }

  .nav { position: absolute; top: 27px; left: 410px; font-size: 10.5px; font-weight: 500; color: var(--white); }
  .nav a { color: inherit; text-decoration: none; position: absolute; white-space: nowrap; }
  .nav .active::after {
    content: ""; position: absolute; left: 0; top: 40px; width: 31px; height: 2px; background: var(--lime);
  }
  .caret { display: inline-block; width: 0; height: 0; margin-left: 6px; vertical-align: middle;
    border-left: 2.5px solid transparent; border-right: 2.5px solid transparent; border-top: 3px solid var(--lime); }
  .btn-clinic {
    position: absolute; left: 782px; top: 18px; width: 93px; height: 32px; background: var(--lime);
    color: var(--white); font-size: 10px; font-weight: 600; display: flex; align-items: center; justify-content: center;
  }
  .menu-icon { position: absolute; left: 894px; top: 28px; }

  .hero-kicker { position: absolute; left: 102px; top: 154px; color: var(--white); font-size: 16px; font-weight: 400; }
  .hero-title { position: absolute; left: 101px; top: 183px; color: var(--white); font-size: 37px; font-weight: 800; letter-spacing: -0.3px; }
  .hero-sub { position: absolute; left: 101px; top: 232px; color: var(--white); font-size: 26px; font-weight: 300; }
  .hero-copy { position: absolute; left: 106px; top: 284px; width: 240px; color: #e6e6e6; font-size: 10px; line-height: 19px; font-weight: 300; }
  .btn-outline {
    position: absolute; display: flex; align-items: center; justify-content: center; font-size: 10px;
  }
  .hero .btn-outline { left: 106px; top: 350px; width: 101px; height: 31px; border: 1px solid var(--lime); color: var(--white); }

  .slider-track { position: absolute; left: 912px; top: 190px; width: 1px; height: 122px; background: rgba(255,255,255,.35); }
  .slider-thumb { position: absolute; left: 911px; top: 234px; width: 2px; height: 35px; background: var(--lime); }

  .video {
    position: absolute; left: 478px; top: 349px; width: 357px; height: 241px;
    border-top: 2px solid #111;
    background: linear-gradient(180deg, #c9cdd0 0%, #b9bec0 45%, #8c9488 60%, #6e8f4a 75%, #5f7f3c 100%);
  }
  .play { position: absolute; left: 151px; top: 93px; }

  .about-rule { position: absolute; left: 102px; top: 516px; width: 1px; height: 158px; background: #333; }
  .about-kicker { position: absolute; left: 120px; top: 568px; font-size: 14px; font-weight: 300; color: #b5b5b5; }
  .about-title { position: absolute; left: 120px; top: 586px; font-size: 27px; font-weight: 700; color: var(--ink); }
  .social { position: absolute; left: 122px; top: 630px; display: flex; gap: 7px; }
  .social span { width: 20px; height: 20px; border-radius: 50%; border: 1px solid var(--line); display: flex; align-items: center; justify-content: center; }
  .social i { width: 6px; height: 6px; border-radius: 50%; background: var(--lime-dark); }
  .about-copy { position: absolute; left: 120px; top: 665px; width: 265px; font-size: 9.6px; line-height: 17.6px; color: var(--text); }
  .about .btn-outline { left: 118px; top: 814px; width: 89px; height: 32px; border: 1px solid var(--line); color: var(--text); }

  .player-photo {
    position: absolute; left: 510px; top: 596px; width: 300px; height: 345px; z-index: 3;
    background: radial-gradient(ellipse 120px 170px at 50% 50%, rgba(110,110,105,.75) 0%, rgba(160,165,95,.55) 45%, rgba(255,255,255,0) 75%);
  }

  .provides-band { position: absolute; left: 286px; top: 874px; width: 652px; height: 46px; background: var(--lime); z-index: 2; }
  .provides-title { position: absolute; left: 25px; top: 3px; font-size: 27px; font-weight: 800; color: var(--white); }

  .cards { position: absolute; left: 102px; top: 920px; width: 733px; height: 264px; display: flex; }
  .card { width: 183.25px; height: 100%; padding: 33px 14px 0 18px; background: var(--card-a); }
  .card:nth-child(even) { background: var(--card-b); }
  .card h3 { font-size: 14.5px; line-height: 19px; font-weight: 700; color: var(--ink); }
  .card .bar { width: 72px; height: 1.5px; background: var(--lime); margin: 13px 0 20px; }
  .card p { font-size: 8.6px; line-height: 17.5px; color: var(--text); }
</style>
</head>
<body>

<header class="hero">
  <div class="hero-photo" role="img" aria-label="Photo of a tennis player serving on a grass court in front of a crowd"></div>

  <div class="brand"><span>Court Fray</span><span class="brand-dot"></span></div>

  <nav class="nav">
    <a class="active" style="left:0">Home</a>
    <a style="left:57px">About</a>
    <a style="left:115px">Tournaments<span class="caret"></span></a>
    <a style="left:214px">Testimonials</a>
    <a style="left:306px">Contact</a>
  </nav>
  <a class="btn-clinic">Clinic Add On</a>
  <svg class="menu-icon" width="18" height="11" viewBox="0 0 18 11" aria-label="Menu">
    <rect x="0" y="0" width="18" height="1.3" fill="#fff"/>
    <rect x="3" y="4.8" width="15" height="1.3" fill="#fff"/>
    <rect x="0" y="9.6" width="18" height="1.3" fill="#fff"/>
  </svg>

  <p class="hero-kicker">Court Fray</p>
  <h1 class="hero-title">Offering Competitive</h1>
  <p class="hero-sub">Tennis Tournaments For Adults</p>
  <p class="hero-copy">Lorem Ipsum is simply dummy text of the printing and typesetting industry.</p>
  <a class="btn-outline">Read More</a>

  <div class="slider-track"></div>
  <div class="slider-thumb"></div>
</header>

<div class="video" role="img" aria-label="Promotional video still of a tennis court by the sea">
  <svg class="play" width="52" height="52" viewBox="0 0 52 52" aria-label="Play video">
    <circle cx="26" cy="26" r="26" fill="rgba(255,255,255,.35)"/>
    <circle cx="26" cy="26" r="21" fill="#fff"/>
    <path d="M22 17 L34 26 L22 35 Z" fill="#111"/>
  </svg>
</div>

<section class="about">
  <div class="about-rule"></div>
  <p class="about-kicker">About us</p>
  <h2 class="about-title">Court Fray</h2>
  <div class="social"><span><i></i></span><span><i></i></span><span><i></i></span></div>
  <p class="about-copy">Welcome our newCourt Fray, was created in 2009 as a company designed to organize and run special tennis events for adults. The company's goal is to coordinate high quality competition and well organized events, while always trying to exceed expectations. Tennis being a sport of ultimate class, it deserves to be treated as such. Court Fray will bring that class...</p>
  <a class="btn-outline">Read More</a>
</section>

<div class="player-photo" role="img" aria-label="Photo of a tennis player in a yellow shirt lunging for a forehand"></div>

<section class="provides">
  <div class="provides-band"><h2 class="provides-title">Court Fray Provides</h2></div>
  <div class="cards">
    <article class="card"><h3>Competition For<br>All Levels</h3><div class="bar"></div><p>All Levels From 2.5-5.0 Are Welcomed And Do Participate, Which Creates The Perfect Environment For Those Interested In The Highest Competition, And For Those Just Looking For A Great Time!</p></article>
    <article class="card"><h3>Competition For<br>All Levels</h3><div class="bar"></div><p>All Levels From 2.5-5.0 Are Welcomed And Do Participate, Which Creates The Perfect Environment For Those Interested In The Highest Competition, And For Those Just Looking For A Great Time!</p></article>
    <article class="card"><h3>Competition For<br>All Levels</h3><div class="bar"></div><p>All Levels From 2.5-5.0 Are Welcomed And Do Participate, Which Creates The Perfect Environment For Those Interested In The Highest Competition, And For Those Just Looking For A Great Time!</p></article>
    <article class="card"><h3>Competition For<br>All Levels</h3><div class="bar"></div><p>All Levels From 2.5-5.0 Are Welcomed And Do Participate, Which Creates The Perfect Environment For Those Interested In The Highest Competition, And For Those Just Looking For A Great Time!</p></article>
  </div>
</section>

</body>
</html>
```